Thank You Card from Pediatric Dentist to Pediatrician - April Showers Promo

We are doing a promo where we are giving local pediatricians and their staff members personalized umbrellas as a thank you for continued referrals of pediatric dental patients. "April Shower Bring May Flowers" Promo. The card will be printed and tied around the umbrella with ribbon... Can be 5x7 or 4x8. Needs to include text and logos below.

Target Market(s)

Pediatricians and their staff members - fun, bright colors

Industry/Entity Type

Medical

Font styles to use
Other font styles liked:
• something fun and bold

Colors
85cae6

Requirements
Must have
• 5x7 or 4x8 single sided card
• must included toothglimmer logo, some umbrella image, and "April Showers Bring May Flowers".
• Needs to include the following text:
• "We are grateful for your continued trust this year. We thank you and wish you and your loved ones a fun-filled summer! Together, we strive to promote the highest level of oral and systemic health for "our kids"!
• Mark Tellwin DMD, Derek Tellwin DMD, Monica Tellwin DMD, Wendy Tellwin COO, Colleen Tellwin DMD, Ruth Tellwin DMD, Associates and Staff"
Nice to have
• see attached copy of our last design crown project
• if room:
• Philadelphia's Premier Pediatric Dental Practice for over 35 Years!

```html
<!DOCTYPE html>
<html lang="en">
<head>
<meta charset="utf-8">
<title>April Showers Thank You Card – Doc Tellwin's Toothglimmer</title>
<link rel="stylesheet" href="https://fonts.googleapis.com/css2?family=Lobster&family=Caveat+Brush&family=Roboto+Condensed:wght@300;400&display=swap">
<style>
  :root {
    --navy: #16308a;
    --teal-band: #1396b8;
    --sky: #3a9fd6;
    --white: #ffffff;
    --umbrella-blue: #8fc9ea;
    --umbrella-green: #9fd8c4;
    --umbrella-yellow: #e6f0a8;
  }
  * { margin: 0; padding: 0; box-sizing: border-box; }
  html, body { width: 1200px; height: 857px; overflow: hidden; background: var(--white); }

  .card {
    position: relative;
    width: 1200px;
    height: 857px;
    overflow: hidden;
    background: var(--white);
  }

  .umbrella-field {
    position: absolute;
    inset: 0;
    background:
      radial-gradient(ellipse 90px 70px at 150px 60px, rgba(230,240,168,.7), transparent 70%),
      radial-gradient(ellipse 130px 90px at 540px 110px, rgba(143,201,234,.6), transparent 70%),
      radial-gradient(ellipse 70px 60px at 45px 330px, rgba(143,201,234,.55), transparent 70%),
      radial-gradient(ellipse 110px 60px at 350px 385px, rgba(159,216,196,.55), transparent 70%),
      radial-gradient(ellipse 60px 45px at 700px 320px, rgba(143,201,234,.55), transparent 70%),
      radial-gradient(ellipse 55px 40px at 835px 370px, rgba(159,216,196,.55), transparent 70%),
      radial-gradient(ellipse 45px 40px at 820px 125px, rgba(159,216,196,.5), transparent 70%),
      radial-gradient(ellipse 40px 30px at 760px 20px, rgba(230,240,168,.6), transparent 70%),
      radial-gradient(ellipse 35px 30px at 910px 45px, rgba(159,216,196,.5), transparent 70%),
      radial-gradient(ellipse 35px 30px at 1155px 100px, rgba(159,216,196,.5), transparent 70%),
      radial-gradient(ellipse 60px 40px at 1010px 820px, rgba(143,201,234,.55), transparent 70%),
      radial-gradient(ellipse 35px 30px at 400px 825px, rgba(159,216,196,.5), transparent 70%),
      radial-gradient(ellipse 30px 25px at 30px 835px, rgba(143,201,234,.5), transparent 70%),
      var(--white);
  }

  .headline {
    position: absolute;
    left: 110px;
    top: 158px;
    width: 590px;
    text-align: center;
    font-family: "Lobster", cursive;
    font-weight: 400;
    color: var(--navy);
    font-size: 80px;
    line-height: 86px;
    letter-spacing: -1px;
  }

  .practice-mark {
    position: absolute;
    left: 903px;
    top: 68px;
    width: 232px;
    height: 232px;
    border-radius: 50%;
    border: 10px solid var(--navy);
    background: var(--white);
    display: flex;
    align-items: center;
    justify-content: center;
    text-align: center;
  }
  .practice-name {
    font-family: "Lobster", cursive;
    color: var(--navy);
    font-size: 30px;
    line-height: 34px;
  }

  .tagline {
    position: absolute;
    left: 900px;
    top: 318px;
    width: 245px;
    text-align: center;
    font-family: "Roboto Condensed", sans-serif;
    font-weight: 400;
    color: var(--sky);
    font-size: 20px;
    line-height: 25.5px;
  }

  .message-band {
    position: absolute;
    left: 0;
    top: 417px;
    width: 1200px;
    height: 364px;
    background: var(--teal-band);
    color: var(--white);
    text-align: center;
  }

  .message {
    position: absolute;
    left: 0;
    top: 22px;
    width: 1200px;
    font-family: "Caveat Brush", cursive;
    font-size: 40px;
    line-height: 52.5px;
  }

  .signature {
    position: absolute;
    left: 0;
    top: 262px;
    width: 1200px;
    font-family: "Roboto Condensed", sans-serif;
    font-weight: 300;
    font-size: 28px;
    line-height: 38px;
  }
</style>
</head>
<body>
  <main class="card">
    <div class="umbrella-field" role="img" aria-label="Scattered watercolor umbrellas in soft blue, green and yellow"></div>

    <h1 class="headline">April Shower Bring<br>May Flowers</h1>

    <div class="practice-mark">
      <span class="practice-name">Doc Tellwin's<br>Toothglimmer</span>
    </div>

    <p class="tagline">Philadelphia's Premier<br>Pediatric Dental Practice<br>for over 35 Years!</p>

    <section class="message-band">
      <p class="message">
        We are grateful for your continued trust this year.<br>
        We thank you and wish you and your loved ones a fun-filled summer!<br>
        Together, we strive to promote<br>
        the highest level of oral and systemic health for "our kids"!
      </p>
      <p class="signature">
        - Mark Tellwin DMD, Derek Tellwin DMD, Monica Tellwin DMD, Wendy Tellwin COO,<br>
        Colleen Tellwin DMD, Ruth Tellwin DMD, Associates and Staff
      </p>
    </section>
  </main>
</body>
</html>
```